Silver Fern Counseling business cards

Dana Korvath, LCPC, NCC
(410)555-0187
www.silverferncounseling.example
dana@silverferncounseling.example

Business cards. I would like it on the same background as pictured. Not on a white business card. I have attached the logo that was done by another designer with artflockly. I am open to looking at single-sided and double-sided designs.

Target Market(s)

teenagers and adults

Industry/Entity Type

mental health

Contact Information for Business Card

Dana Korvath, LCPC, NCC (410)555-0187 dana@silverferncounseling.example

Font styles to use
Other font styles liked:
• Cinzel

Colors

Designer to choose colors to be used in the design.

Requirements
Must have
• logo that is attached

```html
<!DOCTYPE html>
<html lang="en">
<head>
<meta charset="utf-8">
<title>Silver Fern Counseling — Business Cards</title>
<link href="https://fonts.googleapis.com/css2?family=Cinzel:wght@400;600&display=swap" rel="stylesheet">
<style>
  :root {
    --page-bg: #2b2b2d;
    --card-top: #3a4a55;
    --card-bottom: #1d262e;
    --text-light: #e6ecef;
    --text-muted: #c3ccd1;
    --brand: #8fb3bf;
    --rule: #c9d3d8;
  }
  * { margin: 0; padding: 0; box-sizing: border-box; }
  html, body {
    width: 1200px; height: 900px; overflow: hidden;
    background: var(--page-bg);
    font-family: "Cinzel", serif;
  }
  .canvas {
    width: 1200px; height: 900px;
    display: flex; flex-direction: column; align-items: center; justify-content: center;
    gap: 44px;
  }
  .card {
    position: relative;
    width: 640px; height: 366px;
    border-radius: 22px;
    background: linear-gradient(160deg, var(--card-top) 0%, #2a3640 45%, var(--card-bottom) 100%);
    box-shadow: 0 14px 30px rgba(0,0,0,0.45);
    color: var(--text-light);
    overflow: hidden;
  }
  .brand {
    position: absolute;
    display: flex; align-items: center; gap: 14px;
    color: var(--brand);
    font-weight: 600;
    letter-spacing: 0.04em;
    line-height: 1.15;
  }
  .brand-name { display: flex; flex-direction: column; align-items: center; white-space: nowrap; }
  .brand-dot {
    width: 14px; height: 14px; border-radius: 50%;
    background: var(--brand);
    flex: none;
  }
  /* Front */
  .card--front .brand {
    left: 40px; top: 0; width: 280px; height: 310px;
    justify-content: center;
    font-size: 24px;
  }
  .divider {
    position: absolute; left: 345px; top: 56px;
    width: 1px; height: 190px; background: var(--rule);
  }
  .contact {
    position: absolute; left: 380px; top: 66px;
  }
  .contact-name { font-size: 24px; font-weight: 400; letter-spacing: 0.03em; }
  .contact-cred { font-size: 14px; color: var(--text-muted); margin-top: 2px; letter-spacing: 0.04em; }
  .contact-phone { font-size: 15px; margin-top: 22px; letter-spacing: 0.04em; }
  .contact-email {
    position: absolute; left: 0; right: 0; bottom: 46px;
    text-align: center; font-size: 13px; letter-spacing: 0.05em;
  }
  /* Back */
  .card--back .brand {
    left: 0; right: 0; top: 110px;
    justify-content: center;
    font-size: 32px;
  }
  .web {
    position: absolute; left: 0; right: 0; bottom: 62px;
    text-align: center; font-size: 16px; letter-spacing: 0.05em;
  }
</style>
</head>
<body>
  <main class="canvas">
    <section class="card card--front">
      <div class="brand"><span class="brand-dot"></span><span class="brand-name"><span>Silver Fern</span><span>Counseling</span></span></div>
      <div class="divider"></div>
      <div class="contact">
        <p class="contact-name">Dana Korvath</p>
        <p class="contact-cred">LCPC, NCC</p>
        <p class="contact-phone">(410)555-0187</p>
      </div>
      <p class="contact-email">dana@silverferncounseling.example</p>
    </section>
    <section class="card card--back">
      <div class="brand"><span class="brand-dot"></span><span class="brand-name"><span>Silver Fern</span><span>Counseling</span></span></div>
      <p class="web">www.silverferncounseling.example</p>
    </section>
  </main>
</body>
</html>
```